1. Can you describe what your company does?
-> We at R and P Orvex, we do Tube bending and its subassemblies. We can cater to different materials like Mild Steel, Stainless Steel, Aluminium and other non-ferrous material. We collaborate with our clients to make precise components to meet their industry requirements. At R&P Orvex we cater to smaller batches or high-volume requirements as per project needs.

2. Who are your target customers for the website?
-> Automotive, Road construction, warehouse equipment, Data centers, beverage equipment industry, electronics products manufacturers for making fixtures.
-> customers which require tubes and pipe bending, exhaust pipes, sheet metal parts

3. Do you have an existing domain name / website address?
-> This was an existing site: https://www.randporvex.co.in/industry
-> using design.com I created this: https://kitpage.site/RandPOrvexpvtltd
But I am not very satisfied with the one I have created using design.com

4. In addition to a Home Page, which other pages / sections would you like your website to have:
About Us
Contact Us
Products / Services
Office / Mailing Address
Terms and Conditions

For each of the pages / sections you’d like to have, please provide the text (and images, if available) you would like to include.
-> Can you use the content that I have added on design.com : https://kitpage.site/RandPOrvexpvtltd

5. Which of the below are features and functionalities your website will need:
Image Gallery
Videos
Contact Form

6. Please provide the URLs for the social media profiles you'd like to link to the website.
-> Don't have one yet.

```html
<!DOCTYPE html>
<html lang="en">
<head>
<meta charset="utf-8">
<title>R and P Orvex — Tube Bending</title>
<link href="https://fonts.googleapis.com/css2?family=Outfit:wght@300;400;500;600;700;800&display=swap" rel="stylesheet">
<style>
:root{
  --blue:#2f55a4;
  --blue-dark:#25468c;
  --ink:#141414;
  --muted:#4a4a4a;
  --soft:#f2f4f8;
  --card:#f4f5f8;
  --line:#d9dce3;
  --footer:#1c1c1e;
  --ring:#8a8d94;
  --white:#ffffff;
}
*{box-sizing:border-box;margin:0;padding:0}
html,body{width:1200px;height:4274px;overflow:hidden}
body{font-family:"Outfit",sans-serif;color:var(--ink);background:var(--white);position:relative}
.abs{position:absolute}
.center{text-align:center}
h2.section-title{position:absolute;left:0;width:1200px;text-align:center;font-size:36px;font-weight:700;letter-spacing:-0.5px}

/* header */
.site-header{position:absolute;left:0;top:0;width:1200px;height:151px;background:var(--white)}
.brand{position:absolute;left:113px;top:22px;display:flex;flex-direction:column;align-items:center;gap:8px}
.brand-mark{width:58px;height:58px;border:3px solid var(--blue);border-radius:6px}
.brand-name{font-size:15px;color:var(--blue);font-weight:400}
.topbar{position:absolute;left:450px;top:0;width:750px;height:80px;background:var(--soft)}
.cal{position:absolute;left:18px;top:23px;width:50px;height:43px;background:var(--blue);border-radius:3px}
.guide{position:absolute;left:80px;top:24px;font-size:12px;color:var(--muted)}
.guide b{display:block;font-weight:500;color:var(--ink);margin-top:4px}
.topbar .divider{position:absolute;left:274px;top:12px;width:1px;height:56px;background:#b9bcc4}
.top-social{position:absolute;left:354px;top:34px;display:flex;gap:18px}
.top-social span{width:12px;height:12px;border-radius:50%;border:1.5px solid #9aa0aa}
.quote-btn{position:absolute;left:509px;top:20px;width:128px;height:43px;background:var(--blue);color:#fff;font-size:13px;font-weight:500;display:flex;align-items:center;justify-content:center;border-radius:2px}
.nav a{position:absolute;top:110px;font-size:13px;color:var(--ink);text-decoration:none}

/* hero */
.hero{position:absolute;left:0;top:151px;width:1200px;height:564px;background:radial-gradient(ellipse at 62% 78%,#e8a24a 0%,#a2582a 18%,#4a3528 42%,#1d3c44 70%,#132a30 100%)}
.hero .kicker{position:absolute;left:113px;top:167px;font-size:36px;font-weight:700;color:#fff;letter-spacing:-0.8px}
.hero .title{position:absolute;left:113px;top:208px;font-size:78px;font-weight:700;color:#fff;letter-spacing:-2px;line-height:1}
.hero .title .outline{color:transparent;-webkit-text-stroke:1.5px #fff;font-weight:500}
.hero .cta{position:absolute;left:113px;top:317px;width:124px;height:38px;background:#fff;font-size:13px;display:flex;align-items:center;justify-content:center;border-radius:2px}
.slider-nav{position:absolute;left:510px;top:510px;display:flex;align-items:center;gap:10px;color:#fff;font-size:14px;font-weight:500}
.slider-nav i{display:inline-block;width:22px;height:1px;background:#fff}

/* industries */
.ind-card{position:absolute;top:863px;width:264px;height:345px;background:var(--card);border-radius:10px;text-align:center}
.ind-card h3{margin-top:30px;font-size:18px;font-weight:600}
.ind-card p{margin:10px auto 0;width:230px;font-size:11px;line-height:1.5;color:var(--muted)}
.ind-card .more{display:block;margin-top:10px;font-size:11px;font-weight:500;text-decoration:underline}
.ind-photo{position:absolute;left:9px;top:174px;width:246px;height:163px;border-radius:0 0 10px 10px}
.ind-icon{position:absolute;left:105px;top:146px;width:54px;height:53px;background:var(--blue);border:3px solid #fff;border-radius:3px;display:flex;align-items:center;justify-content:center}

/* marquee */
.band{position:absolute;left:0;top:1300px;width:1200px;height:61px;background:var(--blue);overflow:hidden;white-space:nowrap}
.band span{display:inline-block;font-size:30px;font-weight:700;color:#7f9ad4;margin-right:70px;line-height:61px}

/* engineering */
.eng-bg{position:absolute;left:0;top:1361px;width:1200px;height:432px;background:var(--soft)}
.eng-text{position:absolute;left:170px;top:1503px;width:860px;font-size:12px;line-height:1.55;text-align:center;color:var(--muted)}
.video{position:absolute;left:113px;top:1600px;width:974px;height:394px;border-radius:8px;background:linear-gradient(120deg,#3c3a34 0%,#8d8a80 30%,#cfcdc6 48%,#6a665c 70%,#2b2a27 100%)}
.play{position:absolute;left:557px;top:1750px;width:86px;height:86px;border-radius:50%;background:rgba(120,120,120,.85);display:flex;align-items:center;justify-content:center}

/* services */
.svc{position:absolute;top:2145px;width:274px;height:298px;background:var(--card);border-radius:6px;text-align:center}
.svc .thumb{margin:14px auto 0;width:150px;height:110px;border-radius:6px;background:linear-gradient(135deg,#e7e8ec,#a9acb3 55%,#ecedf0)}
.svc hr{border:0;border-top:1px solid var(--line);margin:20px 26px 0}
.svc h3{margin-top:16px;font-size:18px;font-weight:600}
.svc p{margin:8px auto 0;width:226px;font-size:11px;line-height:1.6;color:var(--muted)}
.svc a{display:block;margin-top:8px;font-size:11px;color:var(--blue);text-decoration:underline}

/* gallery */
.g{position:absolute;border-radius:4px}

/* contact */
.lbl{position:absolute;font-size:11px;font-weight:500}
.field{position:absolute;height:51px;width:393px;background:var(--card);border-radius:3px;font-size:11px;color:#8a8e96;padding:18px 20px}
.submit{position:absolute;left:536px;top:3464px;width:128px;height:45px;background:var(--blue);color:#fff;font-size:13px;font-weight:500;display:flex;align-items:center;justify-content:center;border-radius:2px}

/* customers */
.cust{position:absolute;top:3662px;width:153px;height:153px;border-radius:50%;background:#fff;border:1.5px solid var(--ring);box-shadow:0 10px 14px rgba(0,0,0,.08);display:flex;align-items:center;justify-content:center;font-size:15px;font-weight:600;color:var(--ink);text-align:center;white-space:nowrap}

/* footer */
.footer{position:absolute;left:0;top:3928px;width:1200px;height:346px;background:var(--footer);color:#fff}
.footer .f-brand{position:absolute;left:113px;top:86px;display:flex;flex-direction:column;align-items:center;gap:12px}
.footer .f-mark{width:70px;height:70px;border:3px solid #fff;border-radius:6px}
.footer .f-name{font-size:16px}
.footer h4{position:absolute;top:72px;font-size:20px;font-weight:600}
.footer ul{position:absolute;top:114px;list-style:none;font-size:10.5px;line-height:22px}
.f-social{position:absolute;left:937px;top:105px;display:flex;gap:10px}
.f-social span{width:42px;height:42px;border-radius:50%;background:var(--blue)}
.f-social span:nth-child(2){background:#8b8d92}
.f-rule{position:absolute;left:113px;top:298px;width:974px;height:1px;background:#55575c}
.copy{position:absolute;left:0;width:1200px;top:318px;text-align:center;font-size:11px}
.to-top{position:absolute;left:1115px;top:276px;width:48px;height:48px;border-radius:50%;background:var(--blue);display:flex;align-items:center;justify-content:center}
</style>
</head>
<body>

<header class="site-header">
  <div class="brand"><div class="brand-mark"></div><div class="brand-name">R and P Orvex</div></div>
  <div class="topbar">
    <div class="cal"><svg width="50" height="43" viewBox="0 0 50 43"><rect x="16" y="13" width="18" height="17" rx="2" fill="none" stroke="#fff" stroke-width="1.6"/><line x1="16" y1="18" x2="34" y2="18" stroke="#fff" stroke-width="1.6"/><line x1="20" y1="10" x2="20" y2="15" stroke="#fff" stroke-width="1.6"/><line x1="30" y1="10" x2="30" y2="15" stroke="#fff" stroke-width="1.6"/></svg></div>
    <div class="guide">Get Expert Guidance<b><svg width="22" height="8" viewBox="0 0 22 8" style="vertical-align:middle;margin-right:6px"><path d="M0 4h20M16 1l4 3-4 3" stroke="#333" fill="none"/></svg>Schedule</b></div>
    <div class="divider"></div>
    <div class="top-social"><span></span><span></span><span></span><span></span></div>
    <div class="quote-btn">Get a Quote</div>
  </div>
  <nav class="nav">
    <a style="left:286px">Home</a>
    <a style="left:355px">About Us</a>
    <a style="left:442px">Our Services</a>
    <a style="left:549px">Machines and Certifications</a>
    <a style="left:740px">Industries We Serve</a>
    <a style="left:886px">Our Products</a>
    <a style="left:996px">Our Value Chain</a>
  </nav>
</header>

<section class="hero" role="img" aria-label="Welder working with sparks inside a large steel pipe">
  <div class="kicker">The Perfect Fit for your</div>
  <div class="title">Tube Bending <span class="outline">Needs</span></div>
  <div class="cta">Contact Us</div>
  <div class="slider-nav">‹ <span>01</span><i></i><span>02</span><i></i><span>03</span> ›</div>
</section>

<h2 class="section-title" style="top:796px">Industries We serve</h2>

<div class="ind-card" style="left:184px">
  <h3>Automotive</h3>
  <p>We specialize in manufacturing premium automotive components...</p>
  <span class="more">Read More</span>
  <div class="ind-photo" role="img" aria-label="Car on a lift in a service workshop" style="background:linear-gradient(160deg,#c9ced6,#8e98a6 60%,#5d6775)"></div>
  <div class="ind-icon"><svg width="28" height="20" viewBox="0 0 28 20"><circle cx="6" cy="14" r="4" fill="none" stroke="#fff" stroke-width="1.6"/><circle cx="22" cy="14" r="4" fill="none" stroke="#fff" stroke-width="1.6"/><path d="M6 14l6-8h6l4 8" fill="none" stroke="#fff" stroke-width="1.6"/></svg></div>
</div>
<div class="ind-card" style="left:466px">
  <h3>Warehousing Equipment</h3>
  <p>Reliability and durability are essential for warehousing equipment...</p>
  <span class="more">Read More</span>
  <div class="ind-photo" role="img" aria-label="Worker with a pallet truck among cardboard boxes" style="background:linear-gradient(160deg,#c79c6c,#9a7048 55%,#5e4630)"></div>
  <div class="ind-icon"><svg width="26" height="24" viewBox="0 0 26 24"><path d="M4 2v18h18M8 20v-8h8v8M16 8h6" fill="none" stroke="#fff" stroke-width="1.6"/><circle cx="8" cy="21" r="2" fill="#fff"/></svg></div>
</div>
<div class="ind-card" style="left:750px">
  <h3>Road Construction</h3>
  <p>We recognize that road construction projects demand...</p>
  <span class="more">Read More</span>
  <div class="ind-photo" role="img" aria-label="Road roller on fresh asphalt seen from above" style="background:linear-gradient(160deg,#5d6068,#3a3c42 55%,#8a8d94)"></div>
  <div class="ind-icon"><svg width="28" height="22" viewBox="0 0 28 22"><rect x="3" y="10" width="14" height="6" fill="none" stroke="#fff" stroke-width="1.6"/><circle cx="22" cy="15" r="4" fill="none" stroke="#fff" stroke-width="1.6"/><path d="M8 10V4h6l3 6" fill="none" stroke="#fff" stroke-width="1.6"/></svg></div>
</div>

<div class="band"><span>R and P Orvex</span><span>R and P Orvex</span><span>R and P Orvex</span><span>R and P Orvex</span><span>R and P Orvex</span></div>

<div class="eng-bg"></div>
<h2 class="section-title" style="top:1444px">Engineering Flow, Forming Future</h2>
<p class="eng-text">At R&amp;P Orvex, we specialize in precision tube bending and subassembly manufacturing, delivering expert solutions across a diverse range of materials including mild steel, stainless steel, aluminum, and other non-ferrous metals. We partner closely with our clients to engineer precise components that meet exacting industry standards. Whether your project requires small-batch prototyping or high-volume production...</p>
<div class="video" role="img" aria-label="Video still of a tube bending machine forming steel pipes"></div>
<div class="play"><svg width="18" height="18" viewBox="0 0 18 18"><path d="M5 3l10 6-10 6z" fill="#fff"/></svg></div>

<h2 class="section-title" style="top:2076px">Our Service</h2>
<div class="svc" style="left:168px">
  <div class="thumb" role="img" aria-label="Two bent steel pipes"></div><hr>
  <h3>Tube &amp; Pipe Bending</h3>
  <p>We specialize in Tube and Pipe Bending We handle a variety of industrial projects...</p>
  <a>Learn More</a>
</div>
<div class="svc" style="left:463px">
  <div class="thumb" role="img" aria-label="Assorted formed tube ends"></div><hr>
  <h3>Tube End Forming</h3>
  <p>Our tube end forming service is second to none, providing precision and customization for all...</p>
  <a>Learn More</a>
</div>
<div class="svc" style="left:757px">
  <div class="thumb" role="img" aria-label="Insulated exhaust pipe section"></div><hr>
  <h3>Thermal Insulation</h3>
  <p>We offer comprehensive automotive insulation solution including Thermal Insulation for exhaust...</p>
  <a>Learn More</a>
</div>

<h2 class="section-title" style="top:2526px">Our Gallery</h2>
<div class="g" role="img" aria-label="Welder inside a steel pipe" style="left:173px;top:2605px;width:280px;height:172px;background:linear-gradient(135deg,#1f5a6a,#d88a3a 55%,#2a3438)"></div>
<div class="g" role="img" aria-label="Tube bending machine with orange parts" style="left:173px;top:2789px;width:280px;height:173px;background:linear-gradient(135deg,#6c7278,#d8782e 50%,#4b5056)"></div>
<div class="g" role="img" aria-label="Worker grinding metal under blue highlight" style="left:466px;top:2605px;width:281px;height:357px;background:#3f5ea6"></div>
<div class="abs" style="left:556px;top:2737px;width:88px;height:88px;border-radius:50%;background:#fff;display:flex;align-items:center;justify-content:center"><svg width="32" height="32" viewBox="0 0 32 32"><rect x="4" y="12" width="14" height="8" rx="4" transform="rotate(-45 11 16)" fill="none" stroke="#222" stroke-width="2.4"/><rect x="14" y="12" width="14" height="8" rx="4" transform="rotate(-45 21 16)" fill="none" stroke="#222" stroke-width="2.4"/></svg></div>
<div class="g" role="img" aria-label="Welders at work in a workshop" style="left:759px;top:2605px;width:280px;height:172px;background:linear-gradient(135deg,#3d4650,#c0563a 50%,#2c3036)"></div>
<div class="g" role="img" aria-label="Rows of steel pipe bending dies" style="left:759px;top:2789px;width:280px;height:173px;background:linear-gradient(135deg,#2a2c30,#9a9ca2 50%,#3a3c40)"></div>

<h2 class="section-title" style="top:3042px">Contact Us</h2>
<p class="abs center" style="left:0;width:1200px;top:3096px;font-size:11.5px;color:var(--muted)">We collaborate closely with you to ensure your vision becomes a reality.</p>
<span class="lbl" style="left:201px;top:3144px">First Name*</span>
<span class="lbl" style="left:606px;top:3144px">Last Name*</span>
<div class="field" style="left:201px;top:3161px">Enter first name</div>
<div class="field" style="left:606px;top:3161px">Enter last name</div>
<span class="lbl" style="left:201px;top:3225px">Email address*</span>
<span class="lbl" style="left:606px;top:3225px">Phone number*</span>
<div class="field" style="left:201px;top:3242px">Enter email address</div>
<div class="field" style="left:606px;top:3242px">Enter phone number</div>
<span class="lbl" style="left:201px;top:3306px">Message*</span>
<div class="field" style="left:201px;top:3323px;width:798px;height:118px">Type your message</div>
<div class="submit">Submit Now</div>

<h2 class="section-title" style="top:3593px">Our Customers</h2>
<div class="cust" style="left:181px">Torvane</div>
<div class="cust" style="left:352px">Halden Group</div>
<div class="cust" style="left:523px">Brixmotor</div>
<div class="cust" style="left:694px">Pellan Motors</div>
<div class="cust" style="left:865px">Nolvik Group</div>

<footer class="footer">
  <div class="f-brand"><div class="f-mark"></div><div class="f-name">R and P Orvex</div></div>
  <h4 style="left:300px">Quick links</h4>
  <ul style="left:300px"><li>About Us</li><li>Our Services</li><li>Machines and Certifications</li><li>Industries We Serve</li><li>Our Products</li><li>Our Value Chain</li></ul>
  <h4 style="left:510px">Contact Us</h4>
  <ul style="left:510px;line-height:16px;top:116px"><li>Office Address:</li><li>214 "K" Block Nerval</li><li>Industrial Area, Kestra, Pune- 411099</li><li style="margin-top:8px">India</li><li style="margin-top:6px">TEL: +91-9000012345</li><li style="margin-top:6px">EMAIL: randporvex.works@example.com</li></ul>
  <h4 style="left:745px">Services</h4>
  <ul style="left:745px"><li>Tube and Pipe Bending</li><li>Tube End Forming</li><li>Thermal Insulation</li><li>Exhaust Muffler and Silencers</li></ul>
  <h4 style="left:937px">Social Media</h4>
  <div class="f-social"><span></span><span></span><span></span></div>
  <div class="f-rule"></div>
  <div class="to-top"><svg width="14" height="10" viewBox="0 0 14 10"><path d="M2 8l5-5 5 5" stroke="#fff" stroke-width="2" fill="none"/></svg></div>
  <div class="copy">© 2026. All Rights Reserved.</div>
</footer>

</body>
</html>
```